Book Cover (HALF OF ALL WORRIES FADE AWAY)

This book is a series of blog posts from my blog, Notes Fit for Borrowing, which is at glenmarwick.com/blog.
The book is to be called:
HALF OF ALL WORRIES FADE AWAY
And 51 other Notes Fit for Borrowing from the Small Business Sage
(Notes Fit for Borrowing) should be italicized.
My name is Glen Marwick, M.B.A.

I will need three variations for my paperback, hardcover and e-book.
Here are some of the blog titles and their topics:
Preparing Your Small Business For Recession small business recession
Should I Incorporate My Business? Should I Incorporate My Business?
Alternative to Minority Shareholder In Small Private Companies minority shareholder
Small Business Culture – Getting it Right Small Business Culture
What is The Right Way to Fire Someone The Right Way to Fire Someone
The Five Basic Leadership Principles Leadership Principles
10 Tips for New Entrepreneurs – Sure Ways to Increase Your Chances of Success
10 things to consider before becoming an entrepreneur
Strategy vs Biz Plans small business strategy
Closing Sales close the sale
Breakeven break even
Growth makes cash flow suck cash flow issues
Think Twice About Offering Early Payment Discounts prepayment discounts
Firing Customers firing customers
Collections best practices getting paid faster
The Cash Flow Statement cash flow statement
Using Paralegals paralegal
Radical Candor radical candor
Why No is the Second Best Word to a Salesperson's ears value of no
The $8 Million Problem -
Contractor vs Employee contractor vs employee
The Vantrell sales tactic
Systems Turn Goals From Dreams Into Reality Systems vs Goals
The Importance of Realistic Goals stretch goals
Why The Owner Must Review Every Hire hiring for values
Systems Thinking for Small Biz: The Case for SOPs systems thinking
Trust Your Gut business intuition
Grease and friction grease vs friction
Left alone, 90% of problems solve themselves strategic inaction
Referrals Are Great—But Not a Growth Strategy referrals
The Lean Marketing Machine: 7 Hacks to Grow Your Small Business Fast marketing hacks
The Small Business Health Check small business health check
How to Spot a Customer Headed for Trouble — Before They Take You Down With Them customer warning signs
We Are What We Repeatedly Do habits
The Smartest People Know When to Play Dumb playing dumb
Before You Scale, Do the Math unit economics
AI for Small Business: Practical Tools and Use Cases AI for Small Business
Title: Tell Me Right Now—Why Can’t We Raise Your Prices? small business pricing
Why Your Real Competitor Isn’t Who You Think creative destruction
Good Enough Might Be Great satisficing
Bootstrapping: Building Your Business on Your Terms bootstrapping
Building Resilient Companies That Never Have to Bet the Farm bet the farm
We Always Overshoot: From Fiber to Cannabis to AI AI overbuild
A Bias Toward Action bias toward ation
Choosing the Right Business Owner Title business owner title
Jobs to Be Done: Understanding What Your Customers Really Want Jobs to Be Done
Forget Money. Here’s What Really Motivates People. motivation

Target Market(s)

Small business operators, business school students

Industry/Entity Type

Small business

Colors

Designer to choose colors to be used in the design.

Requirements
Should not have
• Should not look cartoonish

```html
<!DOCTYPE html>
<html lang="en">
<head>
<meta charset="utf-8">
<title>Half of All Worries Fade Away — Book Cover</title>
<link rel="stylesheet" href="https://fonts.googleapis.com/css2?family=Anton&family=Crimson+Text:ital@1&display=swap">
<style>
  :root {
    --backdrop: #e9e9e9;
    --cover-dark: #141011;
    --cover-deep: #1f1415;
    --steel: #5e6a6c;
    --ember: #c2371f;
    --glow: #f7b24a;
    --ink-light: #ffffff;
    --ink-soft: #e8e2de;
  }
  * { margin: 0; padding: 0; box-sizing: border-box; }
  html, body {
    width: 1200px; height: 961px; overflow: hidden;
    background: var(--backdrop);
  }
  .canvas {
    position: relative; width: 1200px; height: 961px;
    display: flex; align-items: center; justify-content: center;
  }
  .book-cover {
    position: relative; width: 600px; height: 820px;
    background: var(--cover-dark);
    overflow: hidden;
    box-shadow: 0 18px 40px rgba(0,0,0,0.25);
  }
  .cover-art {
    position: absolute; inset: 0 0 auto 0; height: 560px;
    background:
      radial-gradient(circle at 58% 62%, var(--glow) 0%, rgba(247,178,74,0.55) 10%, rgba(194,55,31,0) 32%),
      linear-gradient(100deg, var(--steel) 0%, #3b3d3e 32%, #7a2a1f 55%, var(--ember) 72%, #5a1a14 100%);
  }
  .cover-art::after {
    content: ""; position: absolute; inset: 0;
    background: linear-gradient(180deg, rgba(20,16,17,0) 45%, var(--cover-dark) 100%);
  }
  .cover-floor {
    position: absolute; inset: 560px 0 0 0;
    background: linear-gradient(180deg, var(--cover-dark) 0%, var(--cover-deep) 100%);
  }
  .cover-text {
    position: absolute; left: 0; right: 0; top: 330px;
    padding: 0 60px 0 40px;
  }
  .book-title {
    font-family: "Anton", sans-serif; font-weight: 400;
    color: var(--ink-light); text-transform: uppercase;
    text-align: center; line-height: 0.92;
    margin-left: 110px;
  }
  .book-title span { display: block; }
  .title-sm { font-size: 70px; }
  .title-md { font-size: 74px; }
  .title-lg { font-size: 124px; }
  .book-subtitle {
    font-family: "Crimson Text", serif; font-style: italic;
    color: var(--ink-soft); font-size: 19px;
    margin-top: 14px; text-align: center;
  }
  .book-author {
    font-family: "Anton", sans-serif; font-weight: 400;
    color: var(--ink-light); font-size: 44px;
    margin-top: 22px; text-transform: uppercase; letter-spacing: 0.5px;
  }
  .book-author small { font-size: 22px; }
</style>
</head>
<body>
<main class="canvas">
  <section class="book-cover">
    <div class="cover-art" role="img" aria-label="Cover illustration: two faces meeting through shattered glass, lit by a warm orange glow"></div>
    <div class="cover-floor"></div>
    <div class="cover-text">
      <h1 class="book-title">
        <span class="title-sm">Half of</span>
        <span class="title-md">All Worries</span>
        <span class="title-lg">Fade</span>
        <span class="title-md">Away</span>
      </h1>
      <p class="book-subtitle">And 51 other Notes Fit for Borrowing from the Small Business Sage</p>
      <p class="book-author">Glen Marwick, <small>M.B.A.</small></p>
    </div>
  </section>
</main>
</body>
</html>
```